Dentistry

Dentist's personal business card. No logo needed. The card shoul deliver the massage of reliability, professionalism, experience.
Please ad the full brief of the project: down the line it says: the winning look should be precise and pristine NO pictures of Teeth, smiles, instruments etc.

The details to be desplaid are:
Dr. Rob Valdoni
Doctor of Dental Surgery
PHD
Web. Www.drvaldoni.com
Email. Rob@drvaldoni.com
Tel 07731482590
Surgery address. 27Bharwick road London SW4 7QN UK
82 Fenwyn Row London SW3 2HT. Uk

Reason: Decided to make the payment unrefundable in order to get more designers involved.

Requirements
Should not have
• Logo, teeth, smile any sort of instruments.

```html
<!DOCTYPE html>
<html lang="en">
<head>
<meta charset="utf-8">
<title>Dr. Rob Valdoni — Business Card</title>
<link href="https://fonts.googleapis.com/css2?family=Open+Sans:wght@400;600&family=Quicksand:wght@400&display=swap" rel="stylesheet">
<style>
  :root {
    --page-bg: #e9e6e1;
    --card-bg: #ffffff;
    --ink: #1c1c1c;
    --ink-soft: #555555;
    --detail-grey: #9a9a9a;
    --bar-black: #111111;
    --rule-grey: #b5b5b5;
  }
  html, body {
    margin: 0;
    padding: 0;
    width: 1200px;
    height: 1000px;
    overflow: hidden;
    background: var(--page-bg);
  }
  .canvas {
    position: relative;
    width: 1200px;
    height: 1000px;
  }
  .card {
    position: absolute;
    width: 577px;
    height: 315px;
    background: var(--card-bg);
    box-shadow: 0 4px 14px rgba(0, 0, 0, 0.18);
  }
  .card--front { left: 33px; top: 33px; }
  .card--back { left: 573px; top: 257px; width: 578px; }

  .edge-bar {
    position: absolute;
    top: 124px;
    width: 6px;
    height: 64px;
    background: var(--bar-black);
  }
  .edge-bar--left { left: 0; }
  .edge-bar--right { right: 0; }

  .wordmark {
    position: absolute;
    left: 0;
    right: 0;
    top: 124px;
    display: flex;
    justify-content: center;
  }
  .wordmark__block {
    display: inline-block;
  }
  .wordmark__name {
    display: block;
    font-family: "Open Sans", sans-serif;
    font-weight: 600;
    font-size: 46px;
    line-height: 1;
    letter-spacing: -1.5px;
    color: var(--ink);
    white-space: nowrap;
  }
  .wordmark__role {
    display: block;
    text-align: right;
    margin-top: 6px;
    padding-right: 2px;
    font-family: "Open Sans", sans-serif;
    font-weight: 600;
    font-size: 10px;
    letter-spacing: 3px;
    color: var(--ink-soft);
    white-space: nowrap;
  }

  .contact {
    position: absolute;
    left: 348px;
    top: 193px;
    font-family: "Quicksand", sans-serif;
    font-size: 11px;
    color: var(--detail-grey);
    letter-spacing: 0.3px;
  }
  .contact__line {
    margin: 0 0 8px;
    line-height: 12px;
  }
  .contact__rule {
    position: absolute;
    left: 330px;
    right: 0;
    top: 254px;
    height: 4px;
    background: linear-gradient(to right, rgba(181,181,181,0), var(--rule-grey) 60%, #8c8c8c);
  }
  .contact__address {
    position: absolute;
    left: 348px;
    top: 270px;
    margin: 0;
    font-family: "Quicksand", sans-serif;
    font-size: 11px;
    line-height: 16px;
    color: var(--detail-grey);
    letter-spacing: 0.3px;
    white-space: nowrap;
  }
</style>
</head>
<body>
  <main class="canvas">
    <section class="card card--front" aria-label="Card front">
      <span class="edge-bar edge-bar--left"></span>
      <span class="edge-bar edge-bar--right"></span>
      <div class="wordmark">
        <div class="wordmark__block">
          <span class="wordmark__name">Dr. Rob Valdoni</span>
          <span class="wordmark__role">DOCTOR OF DENTAL SURGERY · PHD</span>
        </div>
      </div>
    </section>

    <section class="card card--back" aria-label="Card back">
      <div class="contact">
        <p class="contact__line">07731482590</p>
        <p class="contact__line">Rob@drvaldoni.com</p>
        <p class="contact__line">Www.drvaldoni.com</p>
      </div>
      <span class="contact__rule"></span>
      <p class="contact__address">27Bharwick road London SW4 7QN UK<br>82 Fenwyn Row London SW3 2HT. Uk</p>
    </section>
  </main>
</body>
</html>
```